Webdesign mit Grundfarbe Weinrot für allgemeine Steuerberatung
Zielgruppe
Allgemeine Steuerberatung. Zielgruppe ist breit gefächert, allerdings soll die Webseite eher den Jungunternehmer ansprechen.
Aufgabenstellung
Die Grundfarbe sollte weinrot sein.

```html
<!DOCTYPE html>
<html lang="de">
<head>
<meta charset="utf-8">
<title>Steuerberatung K1vra</title>
<link href="https://fonts.googleapis.com/css2?family=Poppins:wght@300;400;500;600;700&display=swap" rel="stylesheet">
<style>
:root{
  --wine:#5c0c26;
  --wine-dark:#3f0818;
  --wine-band:#4d0f22;
  --footer:#4a0d1f;
  --text:#333;
  --muted:#777;
  --light:#f1f1f1;
  --white:#fff;
}
*{margin:0;padding:0;box-sizing:border-box}
html,body{width:1200px;height:2759px;overflow:hidden}
body{font-family:"Poppins",sans-serif;color:var(--text);background:var(--white);position:relative}
.abs{position:absolute}
ul{list-style:none}
.topbar{top:0;left:0;width:1200px;height:31px;background:var(--wine-dark);color:#d9c3ca;font-size:10px;font-weight:300}
.topbar .contact{left:234px;top:9px;display:flex;gap:22px}
.topbar .social{right:234px;top:10px;display:flex;gap:10px}
.dot{width:9px;height:9px;border-radius:50%;background:#bfa3ad;display:block}
.header{top:31px;left:0;width:1200px;height:63px;background:var(--white);border-bottom:1px solid #ddd}
.brand{left:234px;top:6px;color:var(--wine-dark);line-height:1;font-weight:500}
.brand .name{font-size:24px;display:block}
.brand .sub{font-size:9px;display:block;margin-top:3px}
.nav{right:234px;top:26px;display:flex;gap:37px;font-size:9.5px;font-weight:500;color:#222}
.nav .active{color:var(--wine)}
.hero{top:94px;left:0;width:1200px;height:484px;background:linear-gradient(120deg,#7a5a67 0%,#8d6d78 35%,#a07f86 60%,#7c5d67 100%)}
.hero h1{left:234px;top:134px;width:400px;font-size:35px;line-height:43px;font-weight:600;color:var(--white)}
.hero p{left:234px;top:223px;width:480px;font-size:10px;line-height:16px;color:#f2e8eb;font-weight:300}
.btn{background:var(--wine);color:var(--white);font-size:9.5px;font-weight:500;display:flex;align-items:center;justify-content:center}
.hero .btn{left:234px;top:271px;width:90px;height:30px}
.arrow{width:28px;height:28px;border-radius:50%;background:rgba(255,255,255,.3);top:227px}
.photo{display:block}
.service{top:615px;width:231px}
.service .photo{width:231px;height:174px}
.service .body{display:flex;gap:12px;margin-top:22px;padding-left:6px}
.service svg{flex:none}
.service h3{font-size:11.5px;line-height:14px;color:var(--wine);font-weight:500}
.service p{font-size:9.5px;line-height:16px;color:var(--muted);font-weight:300;margin-top:8px}
.stats{top:955px;left:0;width:1200px;height:281px;background:linear-gradient(90deg,#4a1425,#5f2a3b 45%,#4e1a2a)}
.stats h2{top:57px;left:0;width:1200px;text-align:center;color:var(--white);font-size:26px;line-height:30px;font-weight:600}
.stat{top:155px;display:flex;align-items:center;color:var(--white)}
.stat .num{font-size:40px;font-weight:600;line-height:1;padding-right:8px}
.stat .lbl{border-left:1px solid rgba(255,255,255,.6);padding-left:9px;font-size:13px;font-weight:600;line-height:16px}
.stat .lbl small{display:block;font-size:7.5px;font-weight:500;line-height:12px}
.about{top:1236px;left:0;width:1200px;height:404px;background:var(--light)}
.about h2{left:225px;top:62px;font-size:26px;font-weight:600;color:#333}
.about p{left:225px;width:385px;font-size:9.8px;line-height:16px;color:#666;font-weight:300}
.about .photo{left:635px;top:41px;width:340px;height:256px;background:linear-gradient(135deg,#b99a7c,#d8d2cc 50%,#a8b9d6)}
.callback{top:1640px;left:0;width:1200px;height:257px;background:linear-gradient(90deg,#4a1a2c,#5a2a3c 50%,#4b1c2d)}
.callback h2{left:225px;top:49px;width:350px;font-size:22px;line-height:30px;font-weight:600;color:var(--white)}
.callback p{left:225px;top:117px;width:335px;font-size:9.8px;line-height:16px;color:#ead9de;font-weight:300}
.callback label{left:609px;top:53px;font-size:9.5px;font-weight:500;color:var(--white)}
.field{background:var(--white);border:1px solid #ccc;font-size:9.5px;color:#999;padding-left:12px;display:flex;align-items:center}
.callback .btn{left:609px;top:165px;width:71px;height:29px;background:#7a1c36}
.news{top:1897px;left:0;width:1200px;height:520px}
.news h2{left:234px;top:47px;font-size:26px;font-weight:500;color:#333}
.news .all{right:234px;top:70px;font-size:9.5px;font-weight:500;color:#444;text-decoration:underline}
.card{top:112px;width:231px}
.card.shadow{box-shadow:0 2px 8px rgba(0,0,0,.18);height:334px}
.card .photo{width:231px;height:173px}
.card .inner{padding:20px 18px 0}
.meta{font-size:8px;color:#999}
.meta b{color:var(--wine-dark);font-weight:600;margin-left:6px}
.card h3{font-size:11.5px;line-height:14px;font-weight:500;color:#222;margin-top:8px}
.card p{font-size:9.5px;line-height:16px;color:#777;font-weight:300;margin-top:8px}
.card .more{font-size:9.5px;font-weight:500;color:#222;margin-top:12px;display:block}
.footer{top:2417px;left:0;width:1200px;height:277px;background:var(--footer);color:#e6d3d9}
.footer .brand{left:240px;top:55px;color:#9c6c7b;font-weight:400}
.footer .brand .name{font-size:34px}
.footer .brand .sub{font-size:14px}
.footer .about-text{left:234px;top:140px;width:180px;font-size:9.5px;line-height:16px;font-weight:300}
.footer .social{left:234px;top:207px;display:flex;gap:13px}
.footer h4{font-size:13px;font-weight:600;color:var(--white)}
.footer ul{margin-top:20px;font-size:9.8px;font-weight:300;line-height:22.5px}
.footer li::before{content:"›";margin-right:7px}
.bottombar{top:2694px;left:0;width:1200px;height:65px;background:#5a0f25;color:#e6d3d9;font-size:10px;text-align:center;line-height:53px;font-weight:300}
</style>
</head>
<body>

<div class="topbar abs">
  <div class="contact abs">
    <span>☏ Telefon: + 49 641-555018</span>
    <span>✉ Email: info@k1vra-steuerberatung.de</span>
  </div>
  <div class="social abs"><span class="dot"></span><span class="dot"></span><span class="dot"></span><span class="dot"></span></div>
</div>

<header class="header abs">
  <div class="brand abs"><span class="name">Marlene K1vra</span><span class="sub">Steuerberaterin</span></div>
  <nav class="nav abs">
    <span class="active">STARTSEITE</span><span>LEISTUNGEN</span><span>AKTUELLES</span><span>KONTAKT</span>
  </nav>
</header>

<section class="hero abs" role="img" aria-label="Beratungsgespräch am Tisch mit Diagrammen, weinrot getönt">
  <h1 class="abs">Anlageberatung für Kunden</h1>
  <p class="abs">Das Richtige für unsere Kunden tun, egal was passiert. Mit über 15 Jahren Erfahrung stellen wir sicher, dass Sie immer die beste Anleitung erhalten. Wir begleiten Sie auf jedem Schritt</p>
  <span class="btn abs">WEITERLESEN</span>
  <svg class="arrow abs" style="left:18px" viewBox="0 0 28 28"><path d="M16 9l-5 5 5 5" fill="none" stroke="#fff" stroke-width="2"/></svg>
  <svg class="arrow abs" style="right:18px" viewBox="0 0 28 28"><path d="M12 9l5 5-5 5" fill="none" stroke="#fff" stroke-width="2"/></svg>
</section>

<div class="service abs" style="left:234px">
  <div class="photo" role="img" aria-label="Bauplanung mit Helm und Hausmodell" style="background:linear-gradient(135deg,#4f6fa0,#c9c7c2 55%,#e0a040)"></div>
  <div class="body">
    <svg width="34" height="30" viewBox="0 0 34 30" fill="none" stroke="#5c0c26" stroke-width="1.3"><circle cx="17" cy="5" r="3"/><circle cx="6" cy="20" r="3"/><circle cx="28" cy="20" r="3"/><path d="M11 13h12M17 8v5M6 13v4M28 13v4M1 29c0-4 10-4 10 0M23 29c0-4 10-4 10 0"/></svg>
    <div><h3>Leistungen für Selbständige, Gewerbe und Existenzgründer</h3><p>Aliquam placerat commodo fringilla. Nunc pulvinar nulla eu dolor lacinia gravida. Sed aliquam imperdiet est.</p></div>
  </div>
</div>
<div class="service abs" style="left:484px">
  <div class="photo" role="img" aria-label="Geschäftsleute mit Laptop im Büro" style="background:linear-gradient(135deg,#e8ecef,#8a8f96 50%,#2f3338)"></div>
  <div class="body">
    <svg width="32" height="26" viewBox="0 0 32 26" fill="none" stroke="#5c0c26" stroke-width="1.3"><rect x="2" y="2" width="28" height="17"/><path d="M6 14l5-5 4 3 5-6 5 4M11 24h10M16 19v5"/></svg>
    <div><h3>Leistungen für Arbeitnehmer</h3><p>Aliquam consequat dolor nec odio facilisis, nec pellentesque sapien semper. Duis facilisis euismod</p></div>
  </div>
</div>
<div class="service abs" style="left:734px">
  <div class="photo" role="img" aria-label="Münzstapel mit Steuerschild" style="background:linear-gradient(135deg,#f3f3f3,#b8b6b0 50%,#5b5a55)"></div>
  <div class="body">
    <svg width="34" height="26" viewBox="0 0 34 26" fill="none" stroke="#5c0c26" stroke-width="1.3"><path d="M2 12l14-9 16 10-14 9z"/><path d="M2 16l16 9 14-9M2 20l16 5"/></svg>
    <div><h3>Sonstige Einkünfte</h3><p>Sed posuere lacus in viverra dapibus. Phasellus congue quis libero id bibendum. Morbi quis tristique nulla</p></div>
  </div>
</div>

<section class="stats abs" role="img" aria-label="Auswertungsdiagramme auf Papier, weinrot getönt">
  <h2 class="abs">Wir helfen Ihnen, Ihr<br>Geschäft auszubauen</h2>
  <div class="stat abs" style="left:232px"><span class="num">16</span><span class="lbl">LANGJÄHRIGE<br>ERFAHRUNG<small>LERN MEHR</small></span></div>
  <div class="stat abs" style="left:422px"><span class="num">28</span><span class="lbl">PREIS-<br>GEKRÖNTE<small>ALLE ANSEHEN</small></span></div>
  <div class="stat abs" style="left:628px"><span class="num">1</span><span class="lbl">GLOBALE<br>STANDORTE<small>FINDEN SIE UNSEREN STANDORT</small></span></div>
  <div class="stat abs" style="left:800px"><span class="num">+1K</span><span class="lbl">ERFOLGREICHES<br>PROJEKT<small>ALLE ANSEHEN</small></span></div>
</section>

<section class="about abs">
  <h2 class="abs">Steuerberatung K1vra</h2>
  <p class="abs" style="top:110px">Meine Kanzlei berät seit deren Gründung im Jahre 2003 Freiberufler, Gewerbetreibende, Kapitalgesellschaften, Personengesellschaften aus den verschiedensten Branchen sowie gemeinnützige Organisationen. Ebenso unterstützen wir gerne Existenzgründer und nebenberuflich Tätige, wie auch Arbeitnehmer, Vermieter und Rentner.</p>
  <p class="abs" style="top:203px">Mein Team aus erfahrenen Steuerfachangestellten und ich freuen uns, Ihnen kompetent und individuell auf Ihre persönlichen Bedürfnisse abgestimmt, bei Ihren steuerlichen Angelegenheiten zu helfen!</p>
  <div class="photo abs" role="img" aria-label="Hand mit Stift über Diagrammen und Taschenrechner"></div>
</section>

<section class="callback abs" role="img" aria-label="Person am Laptop, weinrot getönt">
  <h2 class="abs">Fordern Sie einen kostenlosen Rückruf an</h2>
  <p class="abs">Möchten Sie telefonisch mit einem unserer Finanzberater sprechen? Senden Sie einfach Ihre Daten und wir werden uns in Kürze bei Ihnen melden. Sie können uns auch eine E-Mail senden, wenn Sie dies bevorzugen.</p>
  <label class="abs">Wie können wir helfen?*</label>
  <div class="field abs" style="left:609px;top:73px;width:293px;height:29px">Diskussion mit Finanzexperten<span style="margin-left:auto;margin-right:10px;font-size:7px">▼</span></div>
  <div class="field abs" style="left:609px;top:120px;width:140px;height:30px;color:#444">Lena Hartwig |</div>
  <div class="field abs" style="left:762px;top:120px;width:140px;height:30px">Telefonnummer *</div>
  <span class="btn abs">SENDEN</span>
</section>

<section class="news abs">
  <h2 class="abs">Aktuelle Meldungen</h2>
  <span class="all abs">Alle Beiträge anzeigen</span>
  <article class="card shadow abs" style="left:234px">
    <div class="photo" role="img" aria-label="Richterhammer und Autoschlüssel" style="background:linear-gradient(135deg,#6b4a33,#c9b8a6 55%,#8d8d8d)"></div>
    <div class="inner"><div class="meta">▦ Seite 1 von 18 &nbsp;|<b>Lohnsteuer</b></div><h3>Aktuelles zum Dienstwagen</h3><p>Die Privatnutzung von Dienstwagen ist für viele Arbeitnehmer ein attraktiver Lohnbestandteil, obgleich sich dieser Vorteil in aller Regel...</p><span class="more">Weiterlesen</span></div>
  </article>
  <article class="card abs" style="left:484px">
    <div class="photo" role="img" aria-label="Hand unterschreibt Vertrag neben Hausmodell" style="background:linear-gradient(135deg,#a88a6c,#e9e4de 55%,#c9c4bd)"></div>
    <div class="inner"><div class="meta">▦ 08.10.2018 &nbsp;|<b>Gewerbeertrag</b></div><h3>Hinzurechnungen von Mietzinsen und Lizenzgebühren</h3><p>Bei der Berechnung der Gewerbesteuer muss der Gewinn aus Gewerbebetrieb um bestimmte Hinzurechnungen ...</p><span class="more">Weiterlesen</span></div>
  </article>
  <article class="card abs" style="left:734px">
    <div class="photo" role="img" aria-label="Hand nimmt Geldscheine aus Geldbörse" style="background:linear-gradient(135deg,#7a7268,#cfc7b0 45%,#5e3f78)"></div>
    <div class="inner"><div class="meta">▦ 08.10.2018 &nbsp;|<b>1-%-Regelung</b></div><h3>Nutzungsentnahme ist nicht auf 50 % zu deckeln</h3><p>Wenn ein privat mitgenutzter Firmen-wagen zu mehr als 50 % betrieblich ge-nutzt wird, muss die private ...</p><span class="more">Weiterlesen</span></div>
  </article>
</section>

<footer class="footer abs">
  <div class="brand abs"><span class="name">Marlene K1vra</span><span class="sub">Steuerberaterin</span></div>
  <p class="about-text abs">Aenean justo sapien, imperdiet vitae tempor viverra, finibus in risus. Etiam non ultrices quam.</p>
  <div class="social abs"><span class="dot"></span><span class="dot"></span><span class="dot"></span><span class="dot"></span></div>
  <div class="abs" style="left:466px;top:62px"><h4>Unternehmen</h4><ul><li>Startseite</li><li>Leistungen</li><li>Aktuelles</li><li>Kontakt</li><li>Impressum</li><li>Datenschutz</li></ul></div>
  <div class="abs" style="left:600px;top:62px"><h4>Leistungen</h4><ul><li>Buchhaltung</li><li>Lohnabrechnungen</li><li>Jahresabschluss</li><li>Steuererklärungen</li><li>Rentner und Pensionäre</li><li>Vermieter</li></ul></div>
  <div class="abs" style="left:761px;top:62px"><h4>&nbsp;</h4><ul><li>Lohnsteuerjahresausgleich</li><li>Veranlagung von Ehegatten und eingetragenen</li><li>Lebenspartnerschaften</li></ul></div>
</footer>

<div class="bottombar abs">© 2018 Steuerberatung K1vra</div>

</body>
</html>
```